Cutting Board Oil Label

I would like a label created for our custom made cutting board oil. The bottle will be clear and come in several different sizes. I have included the current label we use. We would like the information to stay the same, but more aesthetically pleasing and professionally presented. I am also including our logo and the current label of our biggest competitor.

```html
<!DOCTYPE html>
<html lang="en">
<head>
<meta charset="utf-8">
<title>Cutting Board Conditioner Label</title>
<link rel="stylesheet" href="https://fonts.googleapis.com/css2?family=Bebas+Neue&family=Didact+Gothic&family=Roboto+Slab:wght@500&display=swap">
<style>
  :root {
    --teal: #5ccfd3;
    --teal-soft: #8fdde0;
    --gray: #6d6d6d;
    --gray-light: #c9c9c9;
    --ink: #555555;
    --paper: #ffffff;
    --backdrop: #eeeeee;
  }
  * { margin: 0; padding: 0; box-sizing: border-box; }
  html, body {
    width: 1200px; height: 1000px; overflow: hidden;
    background: var(--backdrop);
  }
  .label {
    position: absolute; left: 137px; top: 45px;
    width: 925px; height: 910px;
    background: var(--paper);
    font-family: "Didact Gothic", sans-serif;
    color: var(--ink);
    overflow: hidden;
  }
  .label > * { position: absolute; }

  .bracket-left { left: 4px; top: 57px; width: 12px; height: 787px; background: var(--teal); }
  .bracket-left-cap { left: 4px; top: 57px; width: 58px; height: 10px; background: var(--teal); }
  .stair-icon { left: 74px; top: 61px; width: 42px; height: 60px; }
  .gray-bars { left: 151px; top: 27px; width: 85px; height: 92px; }
  .teal-rules { left: 263px; top: 63px; width: 567px; height: 34px; }
  .bracket-right-cap { left: 830px; top: 57px; width: 63px; height: 27px; background: var(--teal); }
  .bracket-right { left: 882px; top: 57px; width: 11px; height: 146px; background: var(--teal); }

  .product-title {
    left: 22px; top: 150px;
    font-family: "Bebas Neue", sans-serif;
    font-weight: 400;
    font-size: 74px; line-height: 100px;
    color: var(--teal-soft);
    letter-spacing: 0.5px;
  }

  .brand-art {
    left: 466px; top: 108px; width: 337px; height: 122px;
    border-radius: 6px;
    background: linear-gradient(180deg, #e9f8f9 0%, #9fe3e5 100%);
  }
  .brand-name {
    left: 365px; top: 246px; width: 530px; text-align: center;
    font-family: "Didact Gothic", sans-serif;
    font-size: 40px; line-height: 48px; color: var(--gray);
    white-space: nowrap;
  }
  .brand-name .dot {
    display: inline-block; width: 12px; height: 12px; border-radius: 50%;
    background: var(--gray); margin-right: 12px; vertical-align: middle;
  }
  .tagline {
    left: 375px; top: 318px; width: 510px; text-align: center;
    font-family: "Roboto Slab", Georgia, serif; font-weight: 500;
    font-size: 19px; line-height: 24px; color: var(--teal);
    white-space: nowrap;
  }

  .info-box {
    left: 45px; top: 371px; width: 833px; height: 108px;
    border: 3px solid var(--teal);
    text-align: center;
    padding-top: 10px;
  }
  .info-use { font-size: 18px; line-height: 24px; }
  .info-claims { font-size: 24px; line-height: 30px; margin-top: 6px; letter-spacing: 1px; }
  .info-claims span { margin: 0 14px; }
  .info-ingredients { font-size: 15px; line-height: 20px; margin-top: 4px; }

  .gray-bracket { left: 578px; top: 506px; width: 98px; height: 150px; }
  .gray-stripes { left: 872px; top: 527px; width: 47px; height: 108px; }
  .corner-bottom { left: 24px; top: 694px; width: 60px; height: 156px; }

  .directions {
    left: 47px; top: 522px; width: 610px;
    font-size: 24px; line-height: 30px; color: var(--ink);
  }

  .footer {
    left: 0; top: 868px; width: 925px; text-align: center;
    font-size: 20px; line-height: 26px; color: var(--teal);
  }
  .footer .dashes { color: var(--ink); margin: 0 12px; letter-spacing: 3px; }
</style>
</head>
<body>
<main class="label">
  <div class="bracket-left"></div>
  <div class="bracket-left-cap"></div>

  <svg class="stair-icon" viewBox="0 0 42 60" aria-hidden="true">
    <g fill="none" stroke="#5ccfd3" stroke-width="4">
      <path d="M2 38 V2 H28"/>
      <path d="M14 48 V14 H38"/>
      <path d="M26 58 V26 H40"/>
    </g>
  </svg>

  <svg class="gray-bars" viewBox="0 0 85 92" aria-hidden="true">
    <g fill="#6d6d6d">
      <rect x="0" y="0" width="9" height="92"/>
      <rect x="19" y="0" width="9" height="92"/>
      <rect x="38" y="0" width="9" height="92"/>
      <rect x="57" y="0" width="9" height="92"/>
      <rect x="76" y="0" width="9" height="92"/>
    </g>
  </svg>

  <svg class="teal-rules" viewBox="0 0 567 34" preserveAspectRatio="none" aria-hidden="true">
    <g stroke="#8fdde0" stroke-width="2">
      <line x1="0" y1="4" x2="567" y2="2"/>
      <line x1="0" y1="10" x2="567" y2="8"/>
      <line x1="0" y1="16" x2="567" y2="14"/>
      <line x1="0" y1="22" x2="567" y2="20"/>
      <line x1="0" y1="28" x2="567" y2="26"/>
      <line x1="0" y1="33" x2="567" y2="31"/>
    </g>
  </svg>

  <div class="bracket-right-cap"></div>
  <div class="bracket-right"></div>

  <h1 class="product-title">Cutting Board<br>Conditioner</h1>

  <div class="brand-art" role="img" aria-label="Brand emblem artwork area"></div>
  <p class="brand-name"><span class="dot"></span>Pine Hollow Gifts</p>
  <p class="tagline">MEMORABLE GIFTS for MEMORABLE MOMENTS</p>

  <section class="info-box">
    <p class="info-use">For use on cutting boards, butcher blocks, wood utensils, and any other wood products.</p>
    <p class="info-claims">FOOD SAFE<span>-</span>ALL NTURAL</p>
    <p class="info-ingredients">Made with: Beeswax, Mineral Oil, Orange Oil, Lemon Oil, and Vitamin E</p>
  </section>

  <svg class="gray-bracket" viewBox="0 0 98 150" aria-hidden="true">
    <path d="M0 5 H93 V150" fill="none" stroke="#c9c9c9" stroke-width="10"/>
  </svg>

  <svg class="gray-stripes" viewBox="0 0 47 108" aria-hidden="true">
    <g fill="#555555">
      <rect x="0" y="0" width="47" height="8"/>
      <rect x="0" y="25" width="47" height="8"/>
      <rect x="0" y="50" width="47" height="8"/>
      <rect x="0" y="75" width="47" height="8"/>
      <rect x="0" y="100" width="47" height="8"/>
    </g>
  </svg>

  <svg class="corner-bottom" viewBox="0 0 60 156" aria-hidden="true">
    <path d="M5 0 V151 H60" fill="none" stroke="#c9c9c9" stroke-width="10"/>
  </svg>

  <p class="directions">Directions: Apply a generous amount of conditioner with a clean, lint free cloth. For best results, allow board to soak in conditioner overnight. Using a clean, lint free cloth, buff and remove any excess conditioner. For new or unconditioned cutting boards, butcher blocks, or wooden kitchen utensils we recommend repeating the process a second time to ensure your wood is properly sealed. Recondition about once a month (depending on use).</p>

  <p class="footer">www.PineHollowGifts.com<span class="dashes">-----</span>Made in the USA</p>
</main>
</body>
</html>
```